ICT Company specialising in web based information system design and implementation

We need a design for a new company in Australia called "Kestrel Hub". We design and develop customised web based information systems to automate business processes. This design needs to be based around Bootstrap from Plovane (http://plovane.codevault.example/)

Industry/Entity Type

Business

Requirements
Must have
• based on bootstrap plovane, site will be hosted on conrete5 platform. (http://plovane.codevault.example/)

```html
<!DOCTYPE html>
<html lang="en">
<head>
<meta charset="utf-8">
<title>Kestrel Hub — Web Based Information Systems</title>
<link rel="stylesheet" href="https://fonts.googleapis.com/css2?family=Carlito:wght@400;700&family=Questrial&display=swap">
<style>
  :root {
    --ink: #222222;
    --text: #3a3a3a;
    --muted: #555555;
    --brand-blue: #0e9fd3;
    --brand-blue-dark: #0a7fae;
    --accent-red: #c8140f;
    --rule: #bdbdbd;
    --panel-border: #b8b8b8;
    --pill-dark: #4a4a4a;
    --arrow-bg: #4e4e4e;
    --banner-a: #0f7fae;
    --banner-b: #27b2e0;
    --banner-c: #0d95c6;
    --page: #ffffff;
  }
  * { box-sizing: border-box; margin: 0; padding: 0; }
  html, body { width: 1200px; height: 720px; overflow: hidden; background: var(--page); }
  body { position: relative; font-family: "Carlito", "Calibri", sans-serif; color: var(--text); }

  .site-header { position: absolute; left: 0; top: 0; width: 1200px; height: 101px; border-bottom: 2px solid var(--rule); box-shadow: 0 1px 2px rgba(0,0,0,.08); }
  .brand { position: absolute; left: 200px; top: 26px; display: flex; align-items: center; gap: 12px; }
  .brand-mark { width: 52px; height: 52px; border-radius: 50%; background: var(--brand-blue); }
  .brand-name { font-family: "Questrial", sans-serif; font-size: 34px; color: var(--ink); letter-spacing: .5px; }

  .login-btn { position: absolute; left: 953px; top: 18px; width: 48px; height: 17px; border-radius: 9px; background: var(--accent-red); color: #fff; font-size: 12px; font-weight: 700; letter-spacing: 1px; text-align: center; line-height: 17px; }

  .main-nav { position: absolute; top: 64px; left: 0; width: 1200px; height: 24px; }
  .main-nav a { position: absolute; top: 0; height: 24px; line-height: 24px; font-size: 15px; color: var(--muted); text-decoration: none; }
  .main-nav a.is-active { background: var(--brand-blue); color: #fff; border: 1px solid var(--brand-blue-dark); border-radius: 5px; padding: 0 9px; line-height: 22px; }

  .hero { position: absolute; left: 190px; top: 116px; width: 820px; height: 295px; overflow: hidden;
    background: radial-gradient(ellipse at 22% 35%, var(--banner-b) 0%, var(--banner-c) 45%, var(--banner-a) 100%); }
  .hero-copy { position: absolute; left: 29px; top: 102px; color: #fff; font-weight: 700; line-height: 1.45; }
  .hero-copy .lead { font-size: 18px; }
  .hero-copy .headline { font-size: 23px; }
  .hero-copy .sub { font-size: 18px; }
  .hero-visual { position: absolute; left: 352px; top: 26px; width: 452px; height: 232px; border-radius: 6px;
    background: linear-gradient(135deg, #e9eef1 0%, #b9c7cf 55%, #7fa9bd 100%); opacity: .85; }

  .slider-arrow { position: absolute; top: 231px; width: 74px; height: 67px; background: var(--arrow-bg); display: flex; align-items: center; justify-content: center; }
  .slider-arrow.prev { left: 0; background: #5b6b6b; }
  .slider-arrow.next { left: 1127px; }

  .panel { position: absolute; top: 432px; width: 257px; height: 226px; border: 1px solid var(--panel-border); border-radius: 7px; box-shadow: 0 1px 3px rgba(0,0,0,.18); }
  .panel-head { position: absolute; left: 7px; top: 4px; right: 8px; height: 44px; border-bottom: 1px solid var(--rule); display: flex; align-items: center; }
  .panel-icon { width: 38px; height: 38px; margin-left: 5px; border-radius: 6px; }
  .panel-title { font-family: "Questrial", sans-serif; font-size: 21px; color: var(--ink); margin-left: 11px; }
  .panel-list { position: absolute; left: 17px; top: 58px; list-style: none; }
  .panel-list li { height: 24px; line-height: 24px; font-size: 14.5px; color: var(--ink); display: flex; align-items: center; }
  .panel-list li svg { margin-right: 10px; }
  .more-btn { position: absolute; right: 11px; bottom: 10px; width: 40px; height: 13px; border-radius: 7px; background: var(--pill-dark); color: #fff; font-size: 10px; text-align: center; line-height: 13px; }

  .news-item { position: absolute; left: 18px; right: 10px; }
  .news-date { font-size: 15px; color: var(--brand-blue-dark); }
  .news-text { margin-top: 6px; font-size: 12.5px; line-height: 1.2; color: var(--muted); text-align: justify; }

  .site-footer { position: absolute; left: 0; top: 673px; width: 1200px; text-align: center; font-family: "Open Sans", "Carlito", sans-serif; font-size: 10px; color: var(--ink); }
  .footer-nav a { color: var(--ink); text-decoration: none; }
  .footer-nav .sep { margin: 0 6px; }
  .copyright { margin-top: 6px; }
</style>
</head>
<body>
  <header class="site-header">
    <div class="brand">
      <span class="brand-mark"></span>
      <span class="brand-name">Kestrel Hub</span>
    </div>
    <a class="login-btn">Login</a>
    <nav class="main-nav">
      <a class="is-active" style="left:545px">Home</a>
      <a style="left:626px">Tour</a>
      <a style="left:688px">Pricing &amp; Sign Up</a>
      <a style="left:824px">Why Kestrel Hub?</a>
      <a style="left:963px">About</a>
    </nav>
  </header>

  <a class="slider-arrow prev" aria-label="Previous slide">
    <svg width="20" height="30" viewBox="0 0 20 30"><polyline points="16,2 4,15 16,28" fill="none" stroke="#fff" stroke-width="2.5"/></svg>
  </a>
  <a class="slider-arrow next" aria-label="Next slide">
    <svg width="20" height="30" viewBox="0 0 20 30"><polyline points="4,2 16,15 4,28" fill="none" stroke="#fff" stroke-width="2.5"/></svg>
  </a>

  <section class="hero">
    <div class="hero-copy">
      <div class="lead">We design and develop</div>
      <div class="headline">web based information systems</div>
      <div class="sub">to automate business process.</div>
    </div>
    <div class="hero-visual" role="img" aria-label="Two desktop monitors showing website screens"></div>
  </section>

  <section class="panel" style="left:190px">
    <div class="panel-head">
      <div class="panel-icon" role="img" aria-label="Tools icon" style="background:linear-gradient(135deg,#2b8fc9,#9fb3c0)"></div>
      <h2 class="panel-title">Services</h2>
    </div>
    <ul class="panel-list">
      <li><svg width="7" height="9" viewBox="0 0 7 9"><polyline points="1,1 5,4.5 1,8" fill="none" stroke="#0a7fae" stroke-width="2"/></svg>Lorem Ipsum</li>
      <li><svg width="7" height="9" viewBox="0 0 7 9"><polyline points="1,1 5,4.5 1,8" fill="none" stroke="#0a7fae" stroke-width="2"/></svg>Lorem Ipsum</li>
      <li><svg width="7" height="9" viewBox="0 0 7 9"><polyline points="1,1 5,4.5 1,8" fill="none" stroke="#0a7fae" stroke-width="2"/></svg>Lorem Ipsum</li>
      <li><svg width="7" height="9" viewBox="0 0 7 9"><polyline points="1,1 5,4.5 1,8" fill="none" stroke="#0a7fae" stroke-width="2"/></svg>Lorem Ipsum</li>
      <li><svg width="7" height="9" viewBox="0 0 7 9"><polyline points="1,1 5,4.5 1,8" fill="none" stroke="#0a7fae" stroke-width="2"/></svg>Lorem Ipsum</li>
      <li><svg width="7" height="9" viewBox="0 0 7 9"><polyline points="1,1 5,4.5 1,8" fill="none" stroke="#0a7fae" stroke-width="2"/></svg>Lorem Ipsum</li>
    </ul>
    <a class="more-btn">more</a>
  </section>

  <section class="panel" style="left:470px">
    <div class="panel-head">
      <div class="panel-icon" role="img" aria-label="Design tools icon" style="background:linear-gradient(135deg,#3a9bd0,#c9a56a)"></div>
      <h2 class="panel-title">Featured Projects</h2>
    </div>
    <ul class="panel-list">
      <li><svg width="7" height="9" viewBox="0 0 7 9"><polyline points="1,1 5,4.5 1,8" fill="none" stroke="#0a7fae" stroke-width="2"/></svg>Lorem Ipsum</li>
      <li><svg width="7" height="9" viewBox="0 0 7 9"><polyline points="1,1 5,4.5 1,8" fill="none" stroke="#0a7fae" stroke-width="2"/></svg>Lorem Ipsum</li>
      <li><svg width="7" height="9" viewBox="0 0 7 9"><polyline points="1,1 5,4.5 1,8" fill="none" stroke="#0a7fae" stroke-width="2"/></svg>Lorem Ipsum</li>
      <li><svg width="7" height="9" viewBox="0 0 7 9"><polyline points="1,1 5,4.5 1,8" fill="none" stroke="#0a7fae" stroke-width="2"/></svg>Lorem Ipsum</li>
      <li><svg width="7" height="9" viewBox="0 0 7 9"><polyline points="1,1 5,4.5 1,8" fill="none" stroke="#0a7fae" stroke-width="2"/></svg>Lorem Ipsum</li>
      <li><svg width="7" height="9" viewBox="0 0 7 9"><polyline points="1,1 5,4.5 1,8" fill="none" stroke="#0a7fae" stroke-width="2"/></svg>Lorem Ipsum</li>
    </ul>
    <a class="more-btn">more</a>
  </section>

  <section class="panel" style="left:753px">
    <div class="panel-head">
      <div class="panel-icon" role="img" aria-label="Newspaper and globe icon" style="background:linear-gradient(135deg,#e6e6e6,#2f86c8)"></div>
      <h2 class="panel-title">News &amp; Events</h2>
    </div>
    <article class="news-item" style="top:54px">
      <div class="news-date">12-05-2012</div>
      <p class="news-text">Lorem Ipsum is simply dummy text of the printing and typesetting industry.</p>
    </article>
    <article class="news-item" style="top:124px">
      <div class="news-date">12-05-2012</div>
      <p class="news-text">Lorem Ipsum is simply dummy text of the printing and typesetting industry.</p>
    </article>
    <a class="more-btn">more</a>
  </section>

  <footer class="site-footer">
    <nav class="footer-nav">
      <a>Home</a><span class="sep">|</span><a>Tour</a><span class="sep">|</span><a>Pricing &amp; Sign Up</a><span class="sep">|</span><a>Why Kestrel Hub?</a><span class="sep">|</span><a>About</a>
    </nav>
    <p class="copyright">© Copyrights 2012. All Rights Reserved.</p>
  </footer>
</body>
</html>
```